Surface Protection company needs cards

We are a New Zealand company that will apply nanotechnology coatings on surfaces to prevent growth and spread of bacteria, viruses, mold etc with a sprayer. We deal with large corporates, airlines, hospitals and schools so we are after a new modern, simple and clean look that will have great visual impact.
We a company that is focused on prevention and protection.

Company name, Vela Shield

Subtext, Antimicrobial Surface Protection

Logo, VS

Target Market(s)

Hospitals, Transport agencies, Airlines, Corporate entities

Contact Information for Business Card

Company name, VelaShield
Logo, VS

Gareth Tolley
velashieldnz@postbox.example
+64219305562
www.velashield.example.nz

Requirements
Must have
• Simple clean look.
Nice to have
• We apply nano coatings so try and incorporate this into a theme somehow

```html
<!DOCTYPE html>
<html lang="en">
<head>
<meta charset="utf-8">
<title>Vela Shield – Business Cards</title>
<link rel="stylesheet" href="https://fonts.googleapis.com/css2?family=Open+Sans:wght@400;600;700&display=swap">
<style>
  :root {
    --blue: #29a9e1;
    --sky: #3cc0ee;
    --green: #76b843;
    --green-dark: #5fa533;
    --ink: #2a2728;
    --paper: #ffffff;
    --backdrop: #e9e6e1;
  }
  * { box-sizing: border-box; margin: 0; padding: 0; }
  html, body { width: 1200px; height: 903px; overflow: hidden; }
  body {
    background: var(--backdrop);
    font-family: "Open Sans", Arial, sans-serif;
    position: relative;
  }
  .card {
    position: absolute;
    width: 560px;
    height: 320px;
    border-radius: 18px;
    overflow: hidden;
    box-shadow: 0 10px 28px rgba(0,0,0,.22);
  }
  .card-front { left: 60px; top: 110px; background: var(--paper); }
  .card-back { left: 580px; top: 470px; background: var(--ink); }

  .front-art { position: absolute; inset: 0; }

  .brand-front {
    position: absolute;
    right: 50px;
    top: 58px;
    display: flex;
    align-items: center;
    gap: 12px;
  }
  .brand-mark {
    width: 22px; height: 22px;
    background: var(--blue);
  }
  .brand-name {
    font-weight: 400;
    color: var(--blue);
    font-size: 40px;
    letter-spacing: .5px;
    line-height: 1;
  }

  .holder {
    position: absolute;
    left: 0;
    top: 132px;
    padding-left: 42px;
  }
  .holder-flag {
    position: absolute;
    left: 0; top: 4px;
    width: 14px; height: 34px;
    background: var(--sky);
  }
  .holder-name {
    color: var(--green);
    font-weight: 700;
    font-size: 21px;
    line-height: 1.1;
    letter-spacing: .5px;
  }
  .holder-role {
    color: var(--blue);
    font-size: 14px;
    letter-spacing: .5px;
  }

  .contacts {
    position: absolute;
    left: 42px;
    top: 200px;
    list-style: none;
  }
  .contacts li {
    display: flex;
    align-items: center;
    gap: 10px;
    color: var(--blue);
    font-size: 14px;
    letter-spacing: .5px;
    height: 22px;
  }
  .contacts svg { width: 18px; height: 18px; flex: none; }

  .tagline {
    position: absolute;
    right: 48px;
    top: 174px;
    text-align: right;
    color: var(--green-dark);
    font-weight: 700;
    font-size: 14px;
    line-height: 1.25;
    letter-spacing: .4px;
  }

  .brand-back {
    position: absolute;
    inset: 0;
    display: flex;
    align-items: center;
    justify-content: center;
    gap: 16px;
  }
  .brand-back .brand-mark { width: 34px; height: 34px; }
  .brand-back .brand-name { font-size: 64px; }
</style>
</head>
<body>

<section class="card card-front" aria-label="Business card front">
  <svg class="front-art" viewBox="0 0 560 320" width="560" height="320" aria-hidden="true">
    <line x1="248" y1="164" x2="390" y2="164" stroke="var(--blue)" stroke-width="1.6"/>
    <line x1="390" y1="164" x2="560" y2="164" stroke="var(--green)" stroke-width="1.6"/>
    <path d="M0 278 L250 278 C270 278 278 268 286 250 L292 262 C284 282 274 292 256 292 L0 292 Z" fill="var(--green)"/>
    <path d="M0 292 L262 292 C284 292 292 272 300 250 C310 226 322 215 352 215 L560 215 L560 320 L0 320 Z" fill="var(--blue)"/>
    <rect x="0" y="300" width="300" height="20" fill="var(--sky)"/>
  </svg>

  <div class="brand-front">
    <span class="brand-mark"></span>
    <span class="brand-name">Vela Shield</span>
  </div>

  <div class="holder">
    <span class="holder-flag"></span>
    <p class="holder-name">Gareth Tolley</p>
    <p class="holder-role">Managing Director</p>
  </div>

  <ul class="contacts">
    <li>
      <svg viewBox="0 0 18 18"><circle cx="9" cy="9" r="8" fill="none" stroke="var(--green)" stroke-width="1.4"/><path d="M6 5.2 L7.6 5 L8.4 7 L7.4 7.8 C7.9 9 8.9 10 10.1 10.6 L10.9 9.6 L12.9 10.4 L12.7 12 C9 12.4 5.6 9 6 5.2 Z" fill="var(--green)"/></svg>
      +64219305562
    </li>
    <li>
      <svg viewBox="0 0 18 18"><circle cx="9" cy="9" r="8" fill="none" stroke="var(--green)" stroke-width="1.4"/><rect x="5" y="6" width="8" height="6" fill="var(--green)"/><path d="M5 6 L9 9.5 L13 6" fill="none" stroke="#fff" stroke-width="1"/></svg>
      velashieldnz@postbox.example
    </li>
    <li>
      <svg viewBox="0 0 18 18"><circle cx="9" cy="9" r="8" fill="none" stroke="var(--green)" stroke-width="1.4"/><circle cx="9" cy="9" r="4.5" fill="none" stroke="var(--green)" stroke-width="1"/><ellipse cx="9" cy="9" rx="2" ry="4.5" fill="none" stroke="var(--green)" stroke-width="1"/><line x1="4.5" y1="9" x2="13.5" y2="9" stroke="var(--green)" stroke-width="1"/></svg>
      www.velashield.example.nz
    </li>
  </ul>

  <p class="tagline">Antimicrobial Surface<br>Protection</p>
</section>

<section class="card card-back" aria-label="Business card back">
  <div class="brand-back">
    <span class="brand-mark"></span>
    <span class="brand-name">Vela Shield</span>
  </div>
</section>

</body>
</html>
```